New Template design for Website in Wordpress

We are interested in changing our website look at www.cargolinx.com -We also are very interested in Have it done in Wordpress in which we are understanding the search engines are liking a bit more. The website we would want to try working with on this is www.cargolinx.com. We look forward to seeing the different design ideas please just make sure they are in wordpress! Thanks, Marlen

Reason: need more design idea..... We would still like to use our pictures off our site since we paid for them so keep that in mind as well as we would still want the rotating pictures in the head of the page but not in Flash.

```html
<!DOCTYPE html>
<html lang="en">
<head>
<meta charset="utf-8">
<title>Cargolinx – A Diversified Freight Company</title>
<link href="https://fonts.googleapis.com/css2?family=Open+Sans:wght@300;400;600;700;800&family=Alfa+Slab+One&display=swap" rel="stylesheet">
<style>
:root{
  --ink:#1f1f1f;
  --navy:#1b2540;
  --ocean:#0b4a78;
  --red:#8a1410;
  --maroon:#7e1a12;
  --card:#f2f2f2;
  --text:#333;
  --sand:#f2e9cc;
  --white:#fff;
}
*{margin:0;padding:0;box-sizing:border-box}
html,body{width:952px;height:1200px;overflow:hidden}
body{position:relative;background:var(--white);font-family:"Open Sans",Arial,sans-serif;color:var(--text)}
.abs{position:absolute}

.site-header{left:0;top:0;width:952px;height:89px;background:var(--ink);box-shadow:0 4px 8px rgba(0,0,0,.25)}
.brand-name{left:100px;top:16px;font-weight:800;font-size:26px;color:var(--white);letter-spacing:.5px;line-height:1}
.brand-tag{left:100px;top:46px;font-weight:300;font-size:14px;color:var(--white);line-height:1}
.phone{right:103px;top:14px;display:flex;align-items:center;gap:9px;color:var(--white);font-weight:600;font-size:16px;letter-spacing:-.3px}
.main-nav{right:102px;top:57px;display:flex;gap:24px;align-items:center}
.main-nav a{font-weight:800;font-size:11.5px;color:var(--white);text-decoration:none;letter-spacing:-.2px}
.main-nav a.active{background:var(--white);color:var(--red);padding:5px 7px}

.hero{left:100px;top:110px;width:752px;height:300px;border-radius:3px;overflow:hidden;box-shadow:0 18px 16px -14px rgba(0,0,0,.35)}
.hero-photo{left:0;top:0;width:752px;height:300px;background:linear-gradient(170deg,#d7dde4 0%,#b9c4cf 40%,#7f8d9b 65%,#b5703e 85%,#6a7480 100%)}
.hero svg{left:0;top:0}
.hero-title{left:480px;top:98px;width:260px;text-align:center;font-weight:800;font-size:27px;line-height:36px;color:var(--white);letter-spacing:-.5px}
.hero-btn{left:534px;top:192px;width:131px;height:39px;background:var(--maroon);border-bottom:3px solid #5a0f0a;color:var(--white);font-size:15px;font-weight:600;display:flex;align-items:center;justify-content:center;border-radius:2px}
.dots{left:317px;top:264px;width:39px;height:11px;background:var(--white);border-radius:6px;display:flex;gap:3px;align-items:center;justify-content:center}
.dots span{width:6px;height:6px;border-radius:50%;background:var(--navy)}
.dots span.on{background:var(--red)}

.service{top:522px;width:175px;height:116px;background:var(--card);border:1px solid #ddd;border-bottom:5px solid var(--navy);text-align:center;box-shadow:0 10px 10px -10px rgba(0,0,0,.4)}
.service h3{position:absolute;left:0;right:0;top:43px;font-weight:400;font-size:16.5px;line-height:19px;color:var(--red);letter-spacing:-.3px}
.service .more{position:absolute;left:57px;top:94px;width:61px;height:17px;background:var(--navy);color:var(--white);font-size:8.5px;font-weight:600;line-height:17px}
.thumb{top:475px;width:82px;height:82px;border-radius:50%;border:2px solid #ddd}

.about-title{left:101px;top:708px;font-weight:700;font-size:21px;color:var(--navy);letter-spacing:-.3px}
.about-text{left:101px;top:748px;width:540px;font-weight:300;font-size:16px;line-height:21.6px;color:#333;letter-spacing:-.2px}
.about-text p{margin-bottom:8px}

.quote-box{left:675px;top:710px;width:177px;height:148px;background:var(--navy);border-radius:2px;box-shadow:0 12px 10px -10px rgba(0,0,0,.4);text-align:center}
.quote-box h4{position:absolute;left:0;right:0;top:20px;font-family:"Alfa Slab One",Georgia,serif;font-weight:400;font-size:14.5px;line-height:22.5px;color:var(--white)}
.get-now{left:37px;top:100px;width:110px;height:26px;display:flex}
.get-now .lbl{width:70px;background:var(--red);color:var(--white);font-weight:700;font-size:12px;line-height:26px}
.get-now .ico{flex:1;background:var(--maroon);display:flex;align-items:center;justify-content:center}

.footer-links{left:0;top:943px;width:952px;height:197px;background:var(--sand)}
.col{top:30px}
.col h5{font-weight:700;font-size:8px;color:#2a2a2a;margin-bottom:13px}
.col li{list-style:none;font-size:7.3px;color:#444}
.footer-bar{left:0;top:1145px;width:952px;height:55px;background:var(--navy)}
.copy{left:99px;top:20px;font-size:10px;color:var(--white);letter-spacing:-.2px}
.social{right:102px;top:15px;display:flex;gap:7px}
.social span{width:23px;height:23px;border-radius:50%;background:#2c73b5}
</style>
</head>
<body>

<header class="site-header abs">
  <div class="brand-name abs">CARGOLINX</div>
  <div class="brand-tag abs">A DIVERSIFIED FREIGHT COMPANY</div>
  <div class="phone abs">
    <svg width="24" height="24" viewBox="0 0 24 24"><circle cx="12" cy="12" r="10.5" fill="none" stroke="#fff" stroke-width="1.6"/><path d="M8.2 6.5c.6-.3 1.1 0 1.4.6l.8 1.7c.2.5.1 1-.3 1.3l-.7.5c.6 1.5 1.7 2.7 3.2 3.4l.6-.7c.3-.4.9-.5 1.3-.3l1.7.8c.6.3.8.9.5 1.4-.6 1.3-1.8 1.9-3 1.5-3.2-1-5.7-3.5-6.6-6.8-.3-1.2.3-2.8 1.1-3.4z" fill="#fff"/></svg>
    (555)214-0388
  </div>
  <nav class="main-nav abs">
    <a class="active">HOME</a>
    <a>INSURANCE &amp; LEGAL INFO</a>
    <a>FAST FREIGHT QUOTE</a>
  </nav>
</header>

<section class="hero abs">
  <div class="hero-photo abs" role="img" aria-label="Rotating header photo: container ship at sea under a cloudy sky"></div>
  <svg class="abs" width="752" height="300" viewBox="0 0 752 300">
    <polygon points="508,0 752,0 752,300 372,300" fill="#1b2540"/>
    <polygon points="526,0 752,0 752,300 392,300" fill="#0b4a78"/>
    <polyline points="30,153 4,176 30,199" fill="none" stroke="#1b2540" stroke-width="2.5"/>
  </svg>
  <div class="hero-title abs">GET FAST &amp; FREE<br>FREIGHT QUOTES</div>
  <div class="hero-btn abs">Learn more</div>
  <div class="dots abs"><span class="on"></span><span></span><span></span><span></span></div>
</section>

<article class="service abs" style="left:100px"><h3>Freight Forwarding<br>Ocean Services</h3><div class="more">Read More</div></article>
<article class="service abs" style="left:292px"><h3>Flatbed, Step Deck &amp;<br>Piggy Back Service</h3><div class="more">Read More</div></article>
<article class="service abs" style="left:485px"><h3>Dry &amp; Refrigerated<br>Services</h3><div class="more">Read More</div></article>
<article class="service abs" style="left:676px"><h3>Heavy Haul<br>Services</h3><div class="more">Read More</div></article>

<div class="thumb abs" style="left:147px;background:radial-gradient(circle,#4a6f9a,#9fb8d2)" role="img" aria-label="Cargo ship loaded with containers"></div>
<div class="thumb abs" style="left:339px;background:radial-gradient(circle,#6b7a85,#6f8a55)" role="img" aria-label="Flatbed truck on a highway"></div>
<div class="thumb abs" style="left:532px;background:radial-gradient(circle,#e8ecef,#8a9a72)" role="img" aria-label="White refrigerated truck"></div>
<div class="thumb abs" style="left:723px;background:radial-gradient(circle,#b89a2e,#6a7a50)" role="img" aria-label="Heavy haul trailer carrying mining equipment"></div>

<h2 class="about-title abs">About Cargolinx</h2>
<div class="about-text abs">
  <p>Lorem ipsum is a dummy text only. Dolor sit amet, consectetur adipiscing elit. Nullam felis mauris, eleifend ac rhoncus non, lobortis at diam. Pellentesque suscipit nulla sit amet venenatis porttitor. In augue felis.</p>
  <p>Nulla aliquet, nisi id fermentum rutrum, magna quam vestibulum lacus, id ullamcorper lectus justo sed nisl. In vitae ipsum eget eros fermentum facilisis.</p>
</div>

<aside class="quote-box abs">
  <h4>GET A FREE<br>FREIGHT QUOTE<br>IN 2 MINUTES</h4>
  <div class="get-now abs">
    <div class="lbl">Get Now</div>
    <div class="ico"><svg width="15" height="15" viewBox="0 0 16 16"><circle cx="8" cy="8" r="8" fill="#fff"/><path d="M4 8h6M7.5 4.8 10.7 8 7.5 11.2" stroke="#7e1a12" stroke-width="2" fill="none"/></svg></div>
  </div>
</aside>

<footer class="footer-links abs">
  <div class="col abs" style="left:122px"><h5>WORLDWIDE FREIGHT SERVICES</h5><ul style="line-height:20px">
    <li>•Worldwide Shipping Scope</li><li>•Trucking Shipping Services</li><li>•Ocean Shipping Services</li><li>•Insurance &amp; Legal Details</li></ul></div>
  <div class="col abs" style="left:282px"><h5>FREIGHT - TRUCKING SERVICE</h5><ul style="line-height:17.6px">
    <li>•Heavy Equipment Hauling</li><li>•LTL Freight Transport</li><li>•Flatbed Transport</li><li>•Step Deck Transport</li><li>•Dry Van Transport</li><li>•Refrigerated Transport</li><li>•Power Only &amp; Towaway Transport</li></ul></div>
  <div class="col abs" style="left:438px"><h5>OCEAN SHIPPING SERVICES</h5><ul style="line-height:17px">
    <li>•Heavy Equipment Hauling</li><li>•LTL Freight Transport</li><li>•Flatbed Transport</li><li>•Step Deck Transport</li><li>•Dry Van Transport</li><li>•Refrigerated Transport</li><li>•Power Only &amp; Towaway Transport</li></ul></div>
  <div class="col abs" style="left:588px"><h5>WE SHIP IT ALL WORLDWIDE</h5><ul style="line-height:16px">
    <li>•Full Loads</li><li>•LTL-Less Then Full Loads</li><li>•Oversized &amp; Overweight Loads</li><li>•500 LBS to 200,000 LBS (No Limits)</li><li>•Construction &amp; Mining Equipment</li><li>•Mills &amp; Machinery</li><li>•Hay &amp; Alfalfa</li></ul></div>
  <div class="col abs" style="left:741px"><h5>POPLULAR PAGES</h5><ul style="line-height:16px">
    <li>•Equipment Transport</li><li>•Equipment Hauling</li><li>•Shipping Service Areas</li></ul></div>
</footer>

<div class="footer-bar abs">
  <div class="copy abs">Copyright©2014 Cargolinx. All Rights Reserved.</div>
  <div class="social abs"><span></span><span style="background:#1da1e0"></span><span style="background:#3b5a9a"></span></div>
</div>

</body>
</html>
```